Aunt Rolina's Bakery

I am about to create a luxury boutique that specializes in cake baking and cupcake
and ready for parties and special events and order delivery
the logo has already made

Industry/Entity Type

Boutique

Contact Information for Business Card

Email:auntrolinasbakery@maplecrumbmail.com
Instagram: aunt_rolina_bakery
Twitter: xxxxxxx
WhatsApp: xxxxxxx

Requirements
Must have
• luxury design

```html
<!DOCTYPE html>
<html lang="en">
<head>
<meta charset="utf-8">
<title>Aunt Rolina's Bakery — Business Card</title>
<link rel="stylesheet" href="https://fonts.googleapis.com/css2?family=Open+Sans:wght@400;600;700&display=swap">
<style>
  :root {
    --backdrop: #e6e4e1;
    --card: #ffffff;
    --ink: #1f1f1f;
    --ink-soft: #3a3a3a;
    --rose: #d98fa0;
    --band-light: #f1eff0;
    --band-mid: #e3dfe1;
    --icon: #4a4a4a;
  }
  * { box-sizing: border-box; margin: 0; padding: 0; }
  html, body {
    width: 1200px; height: 926px; overflow: hidden;
    background: var(--backdrop);
    font-family: "Open Sans", Arial, sans-serif;
  }
  .business-card {
    position: absolute; left: 100px; top: 177px;
    width: 1000px; height: 572px;
    background: var(--card);
    box-shadow: 0 14px 30px rgba(0,0,0,0.12);
  }
  .brand {
    position: absolute; left: 0; right: 0; top: 90px;
    display: flex; align-items: center; justify-content: center; gap: 22px;
  }
  .brand-dot {
    width: 62px; height: 62px; border-radius: 50%;
    background: var(--rose);
  }
  .brand-name {
    font-weight: 600; font-size: 44px; letter-spacing: 2px;
    color: var(--ink-soft);
  }
  .pattern-band {
    position: absolute; left: 0; right: 0; top: 300px; height: 210px;
    background: linear-gradient(180deg, var(--band-light), var(--band-mid) 50%, var(--band-light));
  }
  .contact-email {
    position: absolute; left: 0; right: 0; top: 326px;
    text-align: center;
    font-weight: 700; font-size: 31px; letter-spacing: 0.5px;
    color: var(--ink);
  }
  .social-row {
    position: absolute; left: 60px; right: 60px; top: 422px;
    display: flex; justify-content: space-between; align-items: center;
  }
  .social-item {
    display: flex; align-items: center; gap: 14px;
    font-size: 22px; color: var(--ink);
  }
  .social-mark {
    width: 42px; height: 42px; border-radius: 50%;
    background: var(--icon);
  }
</style>
</head>
<body>
  <main class="business-card">
    <div class="brand">
      <span class="brand-dot"></span>
      <span class="brand-name">Aunt Rolina's Bakery</span>
    </div>

    <div class="pattern-band" role="img" aria-label="Soft grey floral damask pattern band"></div>

    <p class="contact-email">auntrolinasbakery@maplecrumbmail.com</p>

    <div class="social-row">
      <div class="social-item"><span class="social-mark"></span><span>aunt_rolina_bakery</span></div>
      <div class="social-item"><span class="social-mark"></span><span>xxxxxxx</span></div>
      <div class="social-item"><span class="social-mark"></span><span>xxxxxxx</span></div>
    </div>
  </main>
</body>
</html>
```